The Merchant Crossroads Book Cover

I need a Book Cover Design for a new book:
Title - "The Merchant Crossroads"
Subtitle - "Lessons No Classroom Ever Gave Me"
Author - "Darren Whitlock"

Target Market(s)

Entrepreneur's and Small Business Owners

Industry/Entity Type

Entrepreneur

Font styles to use
Sans Serif

Requirements
Must have
• The branding colors should match our website (Black and accent color: #FBBC05)
• http://MerchantCrossroadsBook.example
• Secondary Subtile (top bar) on front of cover - "A Documentary"
• Back Cover: Brief description, author photo, and the ISBN Number
Nice to have
• A Detour Sign with the word "Detour" on it (or a sign with a "squiggly" line example) ... or a type of image that is on the bottom of Home page of website (road in wilderness).

```html
<!DOCTYPE html>
<html lang="en">
<head>
<meta charset="utf-8">
<title>The Merchant Crossroads — Book Cover</title>
<link rel="stylesheet" href="https://fonts.googleapis.com/css2?family=Source+Sans+3:wght@700;800&family=Cinzel:wght@400&display=swap">
<style>
  :root {
    --cover-black: #000000;
    --brand-yellow: #FBBC05;
    --subtitle-gold: #D39A12;
    --tagline-grey: #6f6f6f;
    --author-ice: #cfe1f2;
    --sky-top: #bfe6f2;
    --sky-low: #eaf6f8;
    --mountain: #7fa8b4;
    --sand-light: #dcb27c;
    --sand-dark: #8a5a2e;
  }
  * { margin: 0; padding: 0; box-sizing: border-box; }
  html, body {
    width: 927px;
    height: 1200px;
    overflow: hidden;
    background: var(--cover-black);
  }
  .cover {
    position: relative;
    width: 927px;
    height: 1200px;
    background: var(--cover-black);
    font-family: "Source Sans 3", "Helvetica Neue", Arial, sans-serif;
  }
  .title {
    position: absolute;
    left: 33px;
    top: 142px;
    color: var(--brand-yellow);
    font-weight: 800;
    font-size: 92px;
    line-height: 86px;
    letter-spacing: -0.5px;
  }
  .tagline {
    position: absolute;
    left: 38px;
    top: 331px;
    color: var(--tagline-grey);
    font-weight: 700;
    font-size: 31px;
    line-height: 1;
  }
  .subtitle {
    position: absolute;
    left: 38px;
    top: 380px;
    color: var(--subtitle-gold);
    font-weight: 700;
    font-size: 31px;
    line-height: 1;
  }
  .road-photo {
    position: absolute;
    left: 0;
    top: 531px;
    width: 927px;
    height: 499px;
    background:
      linear-gradient(to bottom,
        var(--sky-top) 0%,
        var(--sky-low) 10%,
        var(--mountain) 15%,
        var(--sand-light) 22%,
        #c9965e 55%,
        var(--sand-dark) 100%);
  }
  .author {
    position: absolute;
    left: 0;
    width: 927px;
    top: 1150px;
    text-align: center;
    color: var(--author-ice);
    font-family: "Cinzel", "Times New Roman", serif;
    font-size: 22px;
    letter-spacing: 24px;
    line-height: 1;
    padding-left: 24px;
  }
</style>
</head>
<body>
  <main class="cover">
    <h1 class="title">The Merchant<br>Crossroads</h1>
    <p class="tagline">A Documentary</p>
    <p class="subtitle">Lessons No Classroom Ever Gave Me</p>
    <div class="road-photo" role="img" aria-label="Photograph of an empty two-lane desert highway with a yellow centre line, a curve warning sign on the left, and distant blue mountains under a pale sky"></div>
    <p class="author">Darren Whitlock</p>
  </main>
</body>
</html>
```